Velmarone Website Redesign

We need a redesign of the company website.

We're a company, based in the UK, called Velmarone. We develop software for the Healthcare Industry, used by medical professionals throughout the UK on a daily basis.

We have a suite of tools that form the Velmarone Platform, and all are web-based.

We want to communicate that our software is not only innovative but is the best available, easy to use, and provides exceptional quality and RoI.

Additionally, we want our existing customers to be able to see what else we can offer them.

A site map is attached.
Updates

Hi Everyone,

As we approach the deadline for submissions, we’ve shortlisted threedesigns that we felt were the best of the submissions and have asked thedesigners to make some additional changes and produce some content pages so wecan see what’s beneath the Home page in the rest of the site.

Thank you all for your submissions – there was an awful lot ofdisagreement among everyone here over which designs we thought were best andsome of those that haven’t made it into the final three were very well liked.

Those in the final three have been messaged individually and have theirdesigns as the only non-eliminated ones showing. We would ask at this stagethat anyone not in the final three please do no further work or submitadditional designs as we are approaching the deadline and will not be able toprovide sufficient feedback to allow any changes in a short space of time.

Kind regards,
The Velmarone Team

Target Market(s)

Nurses and medical professionals in western-speaking countries, most notably in the UK.

Predominantly, we expect it will be senior medical staff that will be viewing (and using) our website - some will be existing customers and some will be new or potential customers.

Industry/Entity Type

Medical

Requirements
Must have
• Area to showcase and provide information about products.
• Company information - who we are and why you should choose us.
• News and events - blog, archive newsletters, publications, etc.
• Support section for existing customers - FAQ, Forum, Manuals.
• Contact page.
• We also feel that we'd like to have our telephone number and primary email address visible at all times, with an immediate ability for users to request a demonstration.
Nice to have
• A "My Velmarone" area would be nice at some point, though that's something for further down the line.

```html
<!DOCTYPE html>
<html lang="en">
<head>
<meta charset="utf-8">
<title>Velmarone Health</title>
<link rel="stylesheet" href="https://fonts.googleapis.com/css2?family=Arimo:wght@400;700&display=swap">
<style>
:root{
  --page-bg-top:#bcd7f1;
  --page-bg-bottom:#e4f0fb;
  --white:#ffffff;
  --brand:#1b4f93;
  --brand-light:#2f78c4;
  --tagline:#2a86c9;
  --nav-top:#5aa0e0;
  --nav-bottom:#2c6fb8;
  --text:#4a4f57;
  --muted:#7a828c;
  --panel:#eef3f8;
  --panel-line:#d4dde7;
  --login-top:#7fb4e6;
  --login-bottom:#3f82c7;
  --footer-top:#d7e3ef;
  --footer-bottom:#c2d2e2;
  --footer-head:#1b4f93;
  --photo-a:#c9d7e6;
  --photo-b:#8fa9c4;
  --copy-bar:#2c6fb8;
}
*{margin:0;padding:0;box-sizing:border-box}
html,body{width:843px;height:1200px;overflow:hidden}
body{
  font-family:"Arimo",Arial,sans-serif;
  color:var(--text);
  background:linear-gradient(180deg,var(--page-bg-top),var(--page-bg-bottom) 60%,var(--page-bg-top));
  position:relative;
}
.site{position:absolute;left:98px;top:0;width:650px;height:1200px}
.header{position:absolute;left:0;top:0;width:650px;height:118px;background:var(--white)}
.brand{position:absolute;left:18px;top:22px;font-size:27px;font-weight:700;color:var(--brand)}
.tagline{position:absolute;left:18px;top:62px;font-size:14px;font-weight:700;color:var(--tagline)}
.tagline-rule{position:absolute;left:18px;top:84px;width:230px;height:2px;background:var(--tagline)}
.contact{position:absolute;right:20px;top:40px;text-align:left;font-size:12px;font-weight:700;color:var(--brand);line-height:26px}
.nav{position:absolute;left:0;top:122px;width:650px;height:32px;
  background:linear-gradient(180deg,var(--nav-top),var(--nav-bottom));
  display:flex;align-items:center;justify-content:space-around;padding:0 6px}
.nav a{color:var(--white);font-size:12px;text-decoration:none}
.main{position:absolute;left:0;top:154px;width:650px;height:1016px;background:var(--white)}
.hero{position:absolute;left:10px;top:10px;width:630px;height:258px;background:var(--panel);border:1px solid var(--panel-line)}
.hero-photo{position:absolute;left:14px;top:14px;width:320px;height:228px;
  background:linear-gradient(135deg,var(--photo-a),var(--photo-b))}
.hero h1{position:absolute;left:350px;top:70px;font-size:18px;color:var(--brand)}
.hero-rule{position:absolute;left:350px;top:96px;width:260px;height:1px;background:var(--panel-line)}
.hero p{position:absolute;left:350px;font-size:9.5px;line-height:13px;color:var(--text)}
.hero .p1{top:104px;width:255px}
.hero .p2{top:158px;width:120px}
.read-more{position:absolute;left:350px;top:232px;font-size:9px;font-weight:700;color:var(--brand)}
.demo{position:absolute;left:486px;top:162px;width:116px;height:90px;border-radius:8px;
  background:linear-gradient(180deg,var(--nav-top),var(--brand));
  color:var(--white);font-weight:700;font-size:14px;text-align:center;padding-top:22px;line-height:17px}
.demo svg{position:absolute;left:8px;top:8px}
.side{position:absolute;left:8px;top:280px;width:180px}
.login{height:140px;background:linear-gradient(180deg,var(--login-top),var(--login-bottom));
  border-radius:4px;padding:12px 10px;color:var(--white);font-size:9px;font-weight:700}
.login .field{height:14px;background:var(--white);margin:3px 0 8px;border-radius:2px}
.login .forgot{text-align:right;font-weight:400;font-size:8px;margin-top:-4px}
.login .sign{display:inline-block;margin-top:6px;background:var(--white);color:var(--brand);padding:3px 10px;border-radius:3px;font-size:9px}
.side h2{font-size:15px;color:var(--brand);text-align:center;margin:18px 0 6px;border-bottom:1px solid var(--panel-line);padding-bottom:4px}
.item{font-size:9px;line-height:12px;margin-bottom:4px}
.more{display:block;text-align:right;font-size:8.5px;font-weight:700;color:var(--brand);margin-bottom:8px}
.content{position:absolute;left:250px;top:282px;width:390px}
.content h2{font-size:18px;color:var(--brand);border-bottom:1px solid var(--panel-line);padding-bottom:4px;margin-bottom:6px}
.content p{font-size:9.5px;line-height:13px}
.platform{position:relative;height:132px;margin-top:10px}
.platform-photo{position:absolute;left:0;top:0;width:115px;height:125px;background:linear-gradient(135deg,var(--photo-a),var(--photo-b))}
.platform h3,.product h3{font-size:10px;color:var(--brand);margin-bottom:3px}
.platform .text{position:absolute;left:124px;top:0;width:264px}
.products-head{font-size:10px;font-weight:700;color:var(--brand);border-bottom:1px solid var(--panel-line);padding-bottom:3px;margin:16px 0 10px}
.product{position:relative;height:62px;margin-bottom:8px}
.thumb{position:absolute;left:0;top:0;width:52px;height:46px;background:linear-gradient(135deg,var(--photo-a),var(--photo-b))}
.product .text{position:absolute;left:62px;top:0;width:326px}
.footer{position:absolute;left:0;top:1020px;width:650px;height:148px;
  background:linear-gradient(180deg,var(--footer-top),var(--footer-bottom));
  display:flex;padding:14px 18px;gap:10px}
.footer .col{flex:1}
.footer h4{font-size:12px;color:var(--footer-head);margin-bottom:6px}
.footer li{list-style:none;font-size:8.5px;line-height:13px;color:var(--text)}
.footer li::before{content:"» ";color:var(--brand)}
.copy{position:absolute;left:0;top:1172px;width:650px;height:20px;background:var(--copy-bar);
  color:var(--white);font-size:8.5px;text-align:center;line-height:20px}
</style>
</head>
<body>
<div class="site">
  <header class="header">
    <div class="brand">Velmarone Health</div>
    <div class="tagline">Bringing Technology to Healthcare</div>
    <div class="tagline-rule"></div>
    <div class="contact">Call : +44 (0) 207 555 0142<br>Email : support@velmarone-health.com</div>
  </header>
  <nav class="nav">
    <a>Home</a><a>Products &amp; Services ▾</a><a>About Velmarone</a><a>News &amp; Events</a><a>Support</a><a>Contact Velmarone</a><a>My Velmarone</a>
  </nav>
  <main class="main">
    <section class="hero">
      <div class="hero-photo" role="img" aria-label="Photo of a smiling healthcare professional at work"></div>
      <h1>Welcome To Velmarone</h1>
      <div class="hero-rule"></div>
      <p class="p1">In today's changing environment, healthcare organisations globally are faced with challenging pressures to reduce costs while offering improved healthcare services to patients.</p>
      <p class="p2">VELMARONE solutions exploit opportunities offered by the latest technological advances.</p>
      <div class="read-more">Read More</div>
      <div class="demo">
        <svg width="22" height="22" viewBox="0 0 22 22"><circle cx="11" cy="11" r="10" fill="#ffffff"/><path d="M9 6l6 5-6 5z" fill="#1b4f93"/></svg>
        Request<br>a Demo
      </div>
    </section>

    <aside class="side">
      <div class="login">
        USER ID<div class="field"></div>
        PASSWORD<div class="field"></div>
        <div class="forgot">Forgot Password</div>
        <span class="sign">Sign In</span>
      </div>
      <h2>Latest News</h2>
      <p class="item">Lorem Ipsum is simply dummy text of the printing and typesetting industry.</p>
      <span class="more">More »</span>
      <p class="item">Lorem Ipsum is simply dummy text of the printing and typesetting industry.</p>
      <span class="more">More »</span>
      <h2>Our Blog</h2>
      <p class="item">Lorem Ipsum is simply dummy text of the printing and typesetting industry. Lorem Ipsum has been the industry's standard dummy text ever since the 1500s unknown.</p>
      <span class="more">More »</span>
    </aside>

    <section class="content">
      <h2>Velmarone Solutions</h2>
      <p>Velmarone works in partnership with hospitals and healthcare professionals. Our unique approach, our partnership with clinical specialists and our technology platform enables us to deliver highly robust and fit-for-purpose solutions.</p>
      <div class="platform">
        <div class="platform-photo" role="img" aria-label="Photo of clinicians reviewing patient records"></div>
        <div class="text">
          <h3>Our Platform</h3>
          <p>Our technology platform, the Clinical Applications Portal, is a robust service based framework that supports our specialist application development approach. It enables interoperability and integration between Velmarone software modules and other hospital and healthcare systems.</p>
        </div>
      </div>
      <div class="products-head">Our Products and Services include</div>
      <div class="product">
        <div class="thumb" role="img" aria-label="Photo for clinical systems"></div>
        <div class="text"><h3>Clinical Systems</h3><p>Lorem Ipsum is simply dummy text of the printing and typesetting industry.</p><span class="more">More »</span></div>
      </div>
      <div class="product">
        <div class="thumb" role="img" aria-label="Photo for clinical audit tools"></div>
        <div class="text"><h3>Clinical Audit Tools</h3><p>Lorem Ipsum is simply dummy text of the printing and typesetting industry.</p><span class="more">More »</span></div>
      </div>
      <div class="product">
        <div class="thumb" role="img" aria-label="Photo for technology services"></div>
        <div class="text"><h3>Technology Services</h3><p>Lorem Ipsum is simply dummy text of the printing and typesetting industry.</p><span class="more">More »</span></div>
      </div>
    </section>
  </main>

  <footer class="footer">
    <div class="col"><h4>Product &amp; Services</h4><ul><li>Clinical Audit</li><li>Clinical Systems</li><li>Software Development</li><li>Clinical Consultancy</li><li>Case Studies</li><li>Demos</li></ul></div>
    <div class="col"><h4>About Velmarone</h4><ul><li>Leadership Team</li><li>Advisory Board</li><li>Partnerships</li><li>Experienced Clinical Staff</li><li>Medical Solutions Architects</li><li>Client List</li></ul></div>
    <div class="col"><h4>News &amp; Events</h4><ul><li>Monthly News Letters</li><li>Publications</li><li>Events</li><li>Velmarone News Blog</li></ul></div>
    <div class="col"><h4>Support</h4><ul><li>FAQ</li><li>Manuals</li><li>Publications</li><li>User Forums</li></ul></div>
  </footer>
  <div class="copy">Copyright © 2009 velmaronehealth.com &nbsp;|&nbsp; Legal &nbsp;|&nbsp; Contact Us</div>
</div>
</body>
</html>
```